Looking for a cool, modern Cannabis Jar Label

I want you to come up with a better, modern look for a label.

I need it sized to 4” x 3” - I plan to print directly to label printer.

I want you to use Photoshop and deliver me a layered PSD file that I can edit and modify the information as needed..

The label information will need to include places for:
(1) Strain Name - most important part of label - larger font size than rest - example Marlow Frost, KTV #7, Copperleaf Haze
(2) Pricing - for Gram, 1/8, 1/4, 1/2. and Ounce
(3) Strain Designation (Hybrid, Indica or Sativa) - maybe color coded, different color for Indica v. Sativa, just an idea
(4) THC and CBD percentages - for example 23% THC and 0.05% CBD
(5) Farm name - a place where we can add the name/logo of the business that produced the product. example - Bramwell Farms

I have attached a simple mockup showing the information.

I have also attached a few samples of labels we like to give you an idea of the look and feel we are going for.

I am wanting a very clean, modern, classy, readable look.The font will use is Gotham Font.

HI Everyone! Thank you for all of your designs. I am requesting an extension because I need more time to give adequate feedback to the designers. Thank you for your participation and all of your efforts! I will be making a decision soon!

• Gotham Font

Designer to choose colors to be used in the design.

• Thank you for your designs. I am sorry i have been slow in providing feedback, things have been really busy around here!
• I wanted to give some group general feedback. After reviewing all of the designs, there is a common theme among all of the designs that I would like to see changed.
• I would like to see the per gram pricing more prominent on the label. This is what most people are looking for when they are purchasing the product. So I would like to see this stand out from the other pricing tiers. As I think about it, they don't all need to be grouped together in a line. You could have the Per Gram pricing front and center some where and then the other pricing tiers grouped together somewhere else on the label.
• This is the order of importance of items on the label. Items at the the top of the list should be bigger than those below it.
• 1. Strain name
• 2. Pricing - being per gram the most important of all prices
• 3. THC/CBD percentages
• 4. Strain Type (indica, sativa, hybrid)
• 5. Farm name/logo
• When laying out these labels, they will be going on rounded jars and they will be on display. Think of jars with fancy labels in a candy store. They need to be eye catchy, appealing, but easy read.
• Thank you for all of your hard work, everyone is doing a great job.
• Best,
• Nadia

```html
<!DOCTYPE html>
<html lang="en">
<head>
<meta charset="UTF-8">
<title>Marlow Frost – Jar Label</title>
<link rel="stylesheet" href="https://fonts.googleapis.com/css2?family=Montserrat:wght@300;400;500;700;800&display=swap">
<style>
  :root {
    --purple: #5f1478;
    --cream: #fdfde0;
    --ink: #2b2b2b;
    --bg-light: #b87fc5;
    --bg-dark: #74248c;
  }
  * { box-sizing: border-box; margin: 0; padding: 0; }
  html, body {
    width: 1200px;
    height: 923px;
    overflow: hidden;
  }
  body {
    position: relative;
    background: radial-gradient(ellipse at 50% 50%, var(--bg-light) 0%, #a767b8 45%, var(--bg-dark) 100%);
    font-family: "Montserrat", sans-serif;
    color: var(--purple);
  }
  .label {
    position: absolute;
    left: 268px;
    top: 206px;
    width: 684px;
    height: 514px;
    background: var(--cream);
    box-shadow: 0 2px 10px rgba(60, 0, 80, 0.35);
  }
  .label-frame {
    position: absolute;
    left: 15px;
    top: 15px;
    width: 653px;
    height: 487px;
    border: 1.5px solid var(--purple);
    border-radius: 17px 17px 0 0;
  }
  .strain-name {
    position: absolute;
    left: 15px;
    top: 15px;
    width: 653px;
    height: 81px;
    background: var(--purple);
    border-radius: 17px 17px 0 0;
    color: var(--cream);
    font-weight: 300;
    font-size: 52px;
    line-height: 81px;
    text-align: center;
    letter-spacing: 0.5px;
  }
  .strain-type {
    position: absolute;
    left: 0;
    top: 124px;
    width: 100%;
    text-align: center;
    font-weight: 800;
    font-size: 33px;
    letter-spacing: 2px;
  }
  .price {
    position: absolute;
    top: 179px;
    width: 120px;
    height: 121px;
    border: 1.5px solid var(--purple);
  }
  .price .corner {
    position: absolute;
    left: 0;
    top: 0;
    width: 68px;
    height: 68px;
    background: var(--purple);
    clip-path: polygon(0 0, 100% 0, 0 100%);
  }
  .price .unit {
    position: absolute;
    left: 8px;
    top: 2px;
    color: var(--cream);
    font-size: 24px;
    font-weight: 400;
  }
  .price .frac-top {
    position: absolute;
    left: 10px;
    top: 2px;
    color: var(--cream);
    font-size: 24px;
  }
  .price .frac-bottom {
    position: absolute;
    left: 30px;
    top: 30px;
    font-size: 24px;
  }
  .price .amount {
    position: absolute;
    left: 0;
    bottom: 6px;
    width: 100%;
    text-align: center;
    font-size: 36px;
    font-weight: 400;
  }
  .p1 { left: 25px; }
  .p2 { left: 152px; }
  .p3 { left: 280px; }
  .p4 { left: 409px; }
  .p5 { left: 537px; }
  .details {
    position: absolute;
    left: 26px;
    top: 312px;
    width: 630px;
    height: 178px;
    border: 1.5px solid var(--purple);
  }
  .potency {
    position: absolute;
    left: 0;
    top: 0;
    width: 318px;
    height: 100%;
    border-right: 1.5px solid var(--purple);
  }
  .potency-row {
    position: absolute;
    left: 27px;
    width: 264px;
    display: flex;
    justify-content: space-between;
    font-size: 40px;
    font-weight: 400;
    letter-spacing: 2px;
  }
  .row-thc { top: 38px; }
  .row-cbd { top: 96px; }
  .farm {
    position: absolute;
    left: 318px;
    top: 0;
    width: 312px;
    height: 100%;
    display: flex;
    align-items: center;
    justify-content: center;
    gap: 14px;
    color: var(--ink);
  }
  .farm-dot {
    width: 54px;
    height: 54px;
    border: 2px solid var(--ink);
    border-radius: 50%;
  }
  .farm-name {
    font-weight: 800;
    font-size: 28px;
    line-height: 1.05;
    letter-spacing: 1px;
  }
</style>
</head>
<body>
  <div class="label">
    <div class="label-frame"></div>
    <h1 class="strain-name">Marlow Frost</h1>
    <div class="strain-type">SATIVA</div>

    <div class="price p1">
      <div class="corner"></div>
      <span class="unit">g.</span>
      <span class="amount">$10</span>
    </div>
    <div class="price p2">
      <div class="corner"></div>
      <span class="frac-top">1</span><span class="frac-bottom">8</span>
      <span class="amount">$35</span>
    </div>
    <div class="price p3">
      <div class="corner"></div>
      <span class="frac-top">1</span><span class="frac-bottom">4</span>
      <span class="amount">$70</span>
    </div>
    <div class="price p4">
      <div class="corner"></div>
      <span class="frac-top">1</span><span class="frac-bottom">2</span>
      <span class="amount">$140</span>
    </div>
    <div class="price p5">
      <div class="corner"></div>
      <span class="unit">ou</span>
      <span class="amount">$280</span>
    </div>

    <div class="details">
      <div class="potency">
        <div class="potency-row row-thc"><span>THC</span><span>24%</span></div>
        <div class="potency-row row-cbd"><span>CBD</span><span>2%</span></div>
      </div>
      <div class="farm">
        <div class="farm-dot"></div>
        <div class="farm-name">BRAMWELL<br>FARMS</div>
      </div>
    </div>
  </div>
</body>
</html>
```